Ferncrest Dental, LLC business card project

Business card to be designed with current logo.
Dental office- please keep design of card that looks clean and professional.
Please include the following info:
Ferncrest Dental, LLC
Dr. Lorna Pettigrew
2871 Marlowe Street
Bethlehem, PA 18093
610-555-0193
ferncrestdental.office@examplemail.test
Hello everyone-
Reason: Just got back from overseas- will look at all designs and provide feedback. Thank you!
Reason: Polling my friends for the final selection-
thank you to all those that participated- so many talented designers!

```html
<!DOCTYPE html>
<html lang="en">
<head>
<meta charset="utf-8">
<title>Ferncrest Dental, LLC – Business Card</title>
<link rel="stylesheet" href="https://fonts.googleapis.com/css2?family=Source+Sans+3:wght@400&display=swap">
<style>
  :root {
    --card-bg: #ffffff;
    --page-bg: #ffffff;
    --leaf-green: #8cc63f;
    --doctor-green: #5fa83a;
    --soft-green: #d7e9b0;
    --ink: #1a1a1a;
    --edge: #e4e4e4;
  }
  html, body {
    margin: 0;
    padding: 0;
    width: 1200px;
    height: 686px;
    overflow: hidden;
    background: var(--page-bg);
  }
  .card {
    position: relative;
    width: 1200px;
    height: 686px;
    box-sizing: border-box;
    background: var(--card-bg);
    border: 1px solid var(--edge);
    font-family: "Source Sans 3", sans-serif;
    color: var(--ink);
  }
  .corner-mark {
    position: absolute;
    left: 60px;
    top: 84px;
    display: flex;
    align-items: center;
    gap: 10px;
    font-size: 22px;
    color: var(--leaf-green);
    white-space: nowrap;
  }
  .brand {
    position: absolute;
    left: 0;
    right: 0;
    top: 212px;
    display: flex;
    justify-content: center;
    align-items: center;
    gap: 18px;
    font-size: 62px;
    line-height: 1;
    color: var(--leaf-green);
    white-space: nowrap;
  }
  .mark-dot {
    flex: none;
    border-radius: 50%;
    background: var(--leaf-green);
  }
  .corner-mark .mark-dot { width: 18px; height: 18px; }
  .brand .mark-dot { width: 40px; height: 40px; }
  .doctor {
    position: absolute;
    left: 0;
    right: 0;
    top: 336px;
    text-align: center;
    font-size: 46px;
    line-height: 1;
    color: var(--doctor-green);
  }
  .accent-dot {
    position: absolute;
    left: 800px;
    top: 310px;
    width: 70px;
    height: 70px;
    border-radius: 50%;
    background: var(--soft-green);
    opacity: 0.7;
  }
  .contact {
    position: absolute;
    left: 59px;
    top: 478px;
    margin: 0;
    font-style: normal;
    font-size: 29px;
    line-height: 40px;
    color: var(--ink);
  }
</style>
</head>
<body>
  <div class="card">
    <div class="corner-mark"><span class="mark-dot"></span>Ferncrest Dental</div>

    <div class="brand"><span class="mark-dot"></span>Ferncrest Dental, LLC</div>

    <div class="accent-dot" aria-hidden="true"></div>
    <div class="doctor">Dr. Lorna Pettigrew</div>

    <address class="contact">
      2871 Marlowe Street<br>
      Bethlehem, PA 18093<br>
      610-555-0193<br>
      ferncrestdental.office@examplemail.test
    </address>
  </div>
</body>
</html>
```